Fence Contractor Website Design

We are working with Yardline Works. They are a local fencing and automatic gate installer and in need of a new website design.
Some sites to use for inspiration:
https://pinevalebarrier.example
https://marwickrails.example
https://www.tellurpostsandboards.example
https://www.grovanpaneling.example
Thank you for taking the time to consider designing a website for us. We are web developers based in Stockton, CA, USA. Most of our projects go through the same process. Understanding this process may help you win a project with us. We custom-code all of our websites in-house. We don’t have any requirements as to what tools you use for your design, but we prefer Figma files. For any design that we label as four-stars, we send it to the client for review. The client picks the final design they want us to use. Once we complete this process, we will continue to show additional clients all the four-star sites and purchase them later. Your designs will have multiple chances to sell. For better chances of success, we ask that you follow these guidelines.
IMAGES:
If you use any images or icons in the design, we ask that you have a link to the asset so we can purchase the image/icon. Most of the designs we submit do not have the customer’s images on them unless they have some great images. Be creative; show us the feeling you are trying to portray with your image choices. Use any royalty-free site you choose. We subscribe to Stockvane and mainly use their images, but we can purchase images outside of Stockvane.
PLEASE NOTE: we will not submit designs to clients with watermarks on the images.
FONTS:
We ask that you identify the fonts used in the design. This can be done in a message if you want. We typically use Google Fonts and Stockvane Fonts.
CONTENT:
We're always open to different content and ideas. We often submit designs with stock images so the client can see our vision. We typically take pictures after the website launch to use their images with our vision. Lorem Ipsum is fine for paragraphs, but we ask that you write the headers in correct English. We want to be able to show the vision and identify the sections of the website.
INSPIRATION:
We typically add a couple of links in the brief of websites we like to help you get started in your design.
REVISIONS:
We do not often ask for revisions of the designs unless we see something in the design that may not appeal to the client. If there are slight changes that we want to make, we do that in the development process.
FEEDBACK:
We rarely give feedback on designs during the design process. We are working on many website projects and do not have the time to provide feedback. We usually respond if your request is well thought out and asks specific questions, but a note asking “feedback, please” usually goes unanswered.
Number of Pages Required
1 page
Look and feel
Each slider illustrates characteristics of the customer's brand and the style your logo design should communicate.

```html
<!DOCTYPE html>
<html lang="en">
<head>
<meta charset="utf-8">
<title>Yardline Works — Professional Fencing Services</title>
<link rel="stylesheet" href="https://fonts.googleapis.com/css2?family=Krona+One&family=Poppins:ital,wght@0,400;0,500;0,600;0,700;1,400&display=swap">
<style>
:root{
  --navy:#1b2541;
  --red:#e3161c;
  --ink:#222;
  --muted:#555;
  --soft:#f2f2f2;
  --grey:#dcdcdc;
  --white:#fff;
}
*{box-sizing:border-box;margin:0;padding:0}
html,body{width:1200px;height:5263px;overflow:hidden}
body{position:relative;background:var(--white);font-family:'Poppins',sans-serif;color:var(--ink)}
.abs{position:absolute}
.display{font-family:'Krona One',sans-serif;text-transform:uppercase;line-height:1}
.navy{color:var(--navy)}.red{color:var(--red)}
.btn{position:absolute;display:flex;align-items:center;justify-content:center;background:var(--red);color:var(--white);font-weight:600;text-transform:uppercase}
.body-text{font-size:13px;line-height:27px;color:var(--muted)}

/* header */
.site-header{position:absolute;left:0;top:0;width:1200px;height:157px}
.brand{position:absolute;left:65px;top:52px;display:flex;align-items:center;gap:10px;font-family:'Poppins',sans-serif;font-weight:700;font-size:22px;color:var(--navy)}
.brand-mark{width:26px;height:26px;background:var(--red)}
.pill{position:absolute;height:42px;border-radius:21px;display:flex;align-items:center;justify-content:center;color:#fff;font-size:13px;font-weight:500}
.nav{position:absolute;top:97px;left:0;font-size:13px;font-weight:500;color:var(--ink)}
.nav a{position:absolute;white-space:nowrap;text-decoration:none;color:inherit}
.nav .active{color:var(--red);border-bottom:2px solid var(--red);padding:0 8px 8px}

/* hero */
.hero{position:absolute;left:0;top:157px;width:1200px;height:783px;background:var(--soft);overflow:hidden}
.hero-copy{position:absolute;left:68px;top:105px;width:430px}
.hero-copy .eyebrow{font-size:27px}
.hero-copy .kicker{font-size:38px;margin-top:22px}
.hero-copy .big{font-size:70px;margin-top:8px;line-height:1.02}
.hero-copy p{font-size:22px;line-height:38px;color:var(--ink);margin-top:22px;text-align:justify}

/* features */
.feature{position:absolute;top:1010px;width:220px;text-align:center}
.feature svg{display:block;margin:0 auto}
.feature h3{font-family:'Krona One',sans-serif;font-size:20px;line-height:30px;color:var(--ink);margin-top:30px}

/* about */
.about-copy{position:absolute;left:638px;top:1480px;width:412px}
.about-copy h2{font-size:52px}
.about-copy .lead{font-size:18px;font-weight:600;line-height:28px;margin-top:28px;color:var(--ink);text-align:justify}
.about-copy .body-text{margin-top:22px;text-align:justify}

/* services */
.svc-title{position:absolute;left:65px;top:2060px;font-size:50px;line-height:58px}
.svc-rule{position:absolute;left:472px;top:2072px;width:2px;height:84px;background:var(--navy)}
.svc-intro{position:absolute;left:524px;top:2070px;width:585px;font-size:13px;line-height:27px;color:var(--muted)}
.svc-copy{position:absolute;width:525px}
.svc-copy h3{font-size:30px;font-weight:600;color:var(--ink);letter-spacing:-.5px}
.svc-copy .body-text{margin-top:18px;text-align:justify;font-size:13.5px}
.svc-copy.right{text-align:right}
.svc-copy.right .body-text{text-align-last:right}

/* reviews */
.review-title{position:absolute;left:65px;top:3718px;font-size:50px;line-height:58px}
.circle-btn{position:absolute;width:56px;height:56px;border-radius:50%;display:flex;align-items:center;justify-content:center}
.circle-btn.outline{border:2px solid var(--navy);background:#fff}
.circle-btn.fill{background:var(--navy)}
.review-card{position:absolute;top:3660px;width:320px;height:340px;background:#fff;box-shadow:0 4px 14px rgba(0,0,0,.1);text-align:center;padding:38px 28px 0}
.review-card .accent{position:absolute;right:-8px;bottom:-8px;width:220px;height:100px;z-index:-1}
.avatar{width:80px;height:80px;border-radius:50%;margin:0 auto;background:linear-gradient(135deg,#6b5847,#cfc0ad);position:relative}
.quote-dot{position:absolute;right:-6px;bottom:-2px;width:26px;height:26px;border-radius:50%;background:var(--navy);color:#fff;font-size:16px;font-weight:700;line-height:30px}
.review-card p{font-size:13.5px;font-style:italic;line-height:24px;color:var(--muted);margin-top:28px}
.review-card h4{font-size:16px;font-weight:600;margin-top:34px;color:var(--ink)}
.stars{color:#f3b51b;font-size:16px;letter-spacing:2px;margin-top:4px}

/* projects */
.proj-title{position:absolute;left:0;width:1200px;top:4202px;text-align:center;font-size:50px}
.proj-img{position:absolute;top:4305px;width:337px;height:340px}

/* footer */
.site-footer{position:absolute;left:0;top:4865px;width:1200px;height:320px;background:var(--soft)}
.footer-brand{position:absolute;left:180px;top:125px;display:flex;align-items:center;gap:12px;font-weight:700;font-size:30px;color:var(--navy)}
.footer-col h5{font-family:'Krona One',sans-serif;font-size:16px;text-transform:uppercase}
.footer-col{position:absolute;top:95px}
.links{list-style:none;margin-top:34px}
.links li{font-size:13px;line-height:27px;color:var(--ink);display:flex;align-items:center;gap:12px}
.links li::before{content:"";width:8px;height:8px;border-radius:50%;background:var(--red)}
.contact-row{display:flex;gap:18px;margin-top:16px;font-size:12.5px;line-height:16px;color:var(--ink);align-items:flex-start}
.contact-row:first-of-type{margin-top:30px}
.c-icon{width:26px;height:26px;background:var(--red);border-radius:4px;display:flex;align-items:center;justify-content:center;flex:none}
.bottom-bar{position:absolute;left:0;top:5185px;width:1200px;height:78px;background:var(--navy);color:#fff;font-size:12px}
.socials{position:absolute;right:65px;top:26px;display:flex;gap:8px}
.socials span{width:24px;height:24px;background:var(--red);border-radius:3px}
</style>
</head>
<body>

<header class="site-header">
  <div class="brand"><span class="brand-mark"></span>Yardline Works</div>
  <div class="pill" style="left:808px;top:34px;width:118px;background:var(--navy)">CONTACT US</div>
  <div class="pill" style="left:966px;top:34px;width:168px;background:var(--red)">GET A FREE QUOTE</div>
  <nav class="nav">
    <a class="active" style="left:570px">HOME</a>
    <a style="left:672px">ABOUT US</a>
    <a style="left:781px">SERVICES</a>
    <a style="left:886px">PROJECTS</a>
    <a style="left:998px">BLOG</a>
    <a style="left:1076px">REVIEWS</a>
  </nav>
</header>

<section class="hero">
  <svg class="abs" style="left:0;top:0" width="1200" height="783" viewBox="0 0 1200 783">
    <defs>
      <linearGradient id="heroPhoto" x1="0" y1="0" x2="1" y2="1">
        <stop offset="0" stop-color="#c9b9a3"/>
        <stop offset=".45" stop-color="#3b3d35"/>
        <stop offset="1" stop-color="#6d6e5e"/>
      </linearGradient>
    </defs>
    <polygon points="480,783 590,560 700,783" fill="var(--navy)"/>
    <polygon role="img" aria-label="Black steel railing fence along a stone wall" points="640,0 1200,0 1200,783 510,783 590,560 540,390" fill="url(#heroPhoto)"/>
  </svg>
  <div class="hero-copy">
    <div class="display navy eyebrow">Yardline Works</div>
    <div class="display red kicker">Professional</div>
    <div class="display navy big">Fencing<br>Services</div>
    <p>Lorem ipsum dolor sit amet, consecte tur adipiscing elit. Sed porttitor nisi mauris id cursus est condimentum.</p>
  </div>
  <div class="btn" style="left:68px;top:471px;width:302px;height:62px;font-size:21px;text-transform:uppercase">Get A Free Quote</div>
</section>

<!-- features -->
<div class="feature" style="left:98px">
  <svg width="200" height="225" viewBox="0 0 100 115"><polygon points="50,2 97,29 97,86 50,113 3,86 3,29" fill="#fff" stroke="#eee" stroke-width="1.5" style="filter:drop-shadow(0 2px 4px rgba(0,0,0,.12))"/><circle cx="50" cy="57.5" r="31" fill="var(--navy)"/><circle cx="50" cy="52" r="7" fill="none" stroke="#fff" stroke-width="2.5"/><path d="M38 68 q12 -14 24 0" fill="none" stroke="#fff" stroke-width="2.5"/></svg>
  <h3>EXPERIENCE</h3>
</div>
<div class="feature" style="left:365px">
  <svg width="200" height="225" viewBox="0 0 100 115"><polygon points="50,2 97,29 97,86 50,113 3,86 3,29" fill="#fff" stroke="#eee" stroke-width="1.5" style="filter:drop-shadow(0 2px 4px rgba(0,0,0,.12))"/><circle cx="50" cy="57.5" r="31" fill="var(--red)"/><path d="M50 72 C42 62 40 57 40 52 a10 10 0 0 1 20 0 c0 5 -2 10 -10 20z" fill="#fff"/><circle cx="50" cy="52" r="4" fill="var(--red)"/></svg>
  <h3>SIZE &amp;<br>LOCATIONS</h3>
</div>
<div class="feature" style="left:632px">
  <svg width="200" height="225" viewBox="0 0 100 115"><polygon points="50,2 97,29 97,86 50,113 3,86 3,29" fill="#fff" stroke="#eee" stroke-width="1.5" style="filter:drop-shadow(0 2px 4px rgba(0,0,0,.12))"/><circle cx="50" cy="57.5" r="31" fill="var(--navy)"/><circle cx="50" cy="55" r="4.5" fill="#fff"/><circle cx="40" cy="57" r="3.5" fill="#fff"/><circle cx="60" cy="57" r="3.5" fill="#fff"/><path d="M41 70 a9 9 0 0 1 18 0z M33 70 a7 7 0 0 1 10 -4 M67 70 a7 7 0 0 0 -10 -4" fill="#fff"/><text x="50" y="48" text-anchor="middle" font-size="8" fill="#fff">★★★</text></svg>
  <h3>CUSTOMERS</h3>
</div>
<div class="feature" style="left:899px">
  <svg width="200" height="225" viewBox="0 0 100 115"><polygon points="50,2 97,29 97,86 50,113 3,86 3,29" fill="#fff" stroke="#eee" stroke-width="1.5" style="filter:drop-shadow(0 2px 4px rgba(0,0,0,.12))"/><circle cx="50" cy="57.5" r="31" fill="var(--red)"/><circle cx="52" cy="50" r="8" fill="none" stroke="#fff" stroke-width="2.5"/><text x="52" y="53.5" text-anchor="middle" font-size="9" font-weight="700" fill="#fff">$</text><path d="M36 66 l8 -4 h10 l-4 4 M36 66 l6 5 h10 l12 -8" fill="none" stroke="#fff" stroke-width="2.5" stroke-linejoin="round"/></svg>
  <h3>ONLINE<br>SPECIALS</h3>
</div>

<!-- about -->
<svg class="abs" style="left:150px;top:1497px" width="400" height="415" viewBox="0 0 100 104" preserveAspectRatio="none">
  <defs><linearGradient id="gAbout" x1="0" y1="0" x2="1" y2="0"><stop offset="0" stop-color="#a4582c"/><stop offset=".5" stop-color="#3a3a38"/><stop offset="1" stop-color="#7a6f62"/></linearGradient></defs>
  <polygon points="50,2 98,27 98,77 50,102 2,77 2,27" fill="var(--grey)"/>
  <polygon role="img" aria-label="Modern wood and black steel entry gate with keypad" points="57,0 99,24 99,76 57,100 15,76 15,24" fill="url(#gAbout)"/>
</svg>
<div class="about-copy">
  <h2 class="display"><span class="navy">About</span> <span class="red">Us</span></h2>
  <p class="lead">Lorem ipsum dolor sit amet, consectetur adipiscing elit. Etiam in vestibu lum urna.</p>
  <p class="body-text">Lorem ipsum dolor sit amet, consectetur adipiscing elit. Etiam in vestibu lum urna. Quisque in lectus non sem con sequat varius mattis id odio. Mauris sed libero a velit pel lentesque volutpat. Donec sed augue congue, consequat eros in, fringilla ante. Inter dum et malesuada fames ac ante ipsum primis in faucibus. Lorem ipsum dolor sit amet, consecte tur adipiscing elit. Etiam in vestibulum urna.</p>
</div>
<div class="btn" style="left:638px;top:1860px;width:168px;height:46px;font-size:13px">Read More</div>

<!-- services -->
<h2 class="display svc-title"><span class="navy">Our</span><br><span class="red">Services</span></h2>
<div class="svc-rule"></div>
<p class="svc-intro">Lorem ipsum dolor sit amet, consectetur adipiscing elit, sed do eiusmod tempor inc ididunt ut labore et dolore magna aliqua. Quis ipsum suspendisse ultrices gravida. Risus comm odo viverra maecenas accumsan lacus vel facilisis.</p>

<div class="svc-copy right" style="left:112px;top:2298px">
  <h3>FENCE INSTALLATION</h3>
  <p class="body-text">Lorem ipsum dolor sit amet, consectetur adipiscing elit. Integer porttitor nisl in nunc finibus fermentum ac volutpat ligula. Duis lacinia magna vel tortor condimentum congue. Quisque consequat, neque nec tincidunt pharetra, ex arcu porttitor massa, vel pharetra risus eros in lorem. Sed ac cumsan orci at sodales facilisis. Sed et faucibus tortor.</p>
</div>
<div class="btn" style="left:490px;top:2518px;width:146px;height:40px;font-size:13px">Read More</div>
<svg class="abs" style="left:690px;top:2222px" width="396" height="410" viewBox="0 0 100 104" preserveAspectRatio="none">
  <defs><linearGradient id="gSvc1" x1="0" y1="0" x2="0" y2="1"><stop offset="0" stop-color="#8fb8de"/><stop offset=".5" stop-color="#9aa3a8"/><stop offset="1" stop-color="#5f6660"/></linearGradient></defs>
  <polygon points="50,2 98,27 98,77 50,102 2,77 2,27" fill="var(--grey)"/>
  <polygon role="img" aria-label="New galvanized steel fence installed beside a rail crossing" points="44,0 88,24 88,76 44,100 0,76 0,24" fill="url(#gSvc1)"/>
</svg>

<svg class="abs" style="left:115px;top:2680px" width="396" height="410" viewBox="0 0 100 104" preserveAspectRatio="none">
  <defs><linearGradient id="gSvc2" x1="0" y1="0" x2="1" y2="1"><stop offset="0" stop-color="#1d2a3a"/><stop offset=".5" stop-color="#4a5566"/><stop offset="1" stop-color="#2c2620"/></linearGradient></defs>
  <polygon points="50,2 98,27 98,77 50,102 2,77 2,27" fill="var(--grey)"/>
  <polygon role="img" aria-label="Welder fabricating a steel fence frame with sparks" points="44,0 88,24 88,76 44,100 0,76 0,24" fill="url(#gSvc2)"/>
</svg>
<div class="svc-copy" style="left:560px;top:2756px">
  <h3>CUSTOM FABRICATION</h3>
  <p class="body-text">Lorem ipsum dolor sit amet, consectetur adipiscing elit. Integer porttitor nisl in nunc finibus fermentum ac volutpat ligula. Duis lacinia magna vel tortor condimentum congue. Quisque consequat, neque nec tincidunt pharetra, ex arcu porttitor massa, vel pharetra risus eros in lorem. Sed ac cumsan orci at sodales facilisis. Sed et faucibus tortor.</p>
</div>
<div class="btn" style="left:564px;top:2976px;width:146px;height:40px;font-size:13px">Read More</div>

<div class="svc-copy right" style="left:112px;top:3184px">
  <h3>AUTOMATIC GATES</h3>
  <p class="body-text">Lorem ipsum dolor sit amet, consectetur adipiscing elit. Integer porttitor nisl in nunc finibus fermentum ac volutpat ligula. Duis lacinia magna vel tortor condimentum congue. Quisque consequat, neque nec tincidunt pharetra, ex arcu porttitor massa, vel pharetra risus eros in lorem. Sed ac cumsan orci at sodales facilisis. Sed et faucibus tortor.</p>
</div>
<div class="btn" style="left:490px;top:3404px;width:146px;height:40px;font-size:13px">Read More</div>
<svg class="abs" style="left:690px;top:3108px" width="396" height="410" viewBox="0 0 100 104" preserveAspectRatio="none">
  <defs><linearGradient id="gSvc3" x1="0" y1="0" x2="1" y2="0"><stop offset="0" stop-color="#3e3a3a"/><stop offset=".6" stop-color="#5a4b40"/><stop offset="1" stop-color="#8a8270"/></linearGradient></defs>
  <polygon points="50,2 98,27 98,77 50,102 2,77 2,27" fill="var(--grey)"/>
  <polygon role="img" aria-label="Technician wiring an automatic gate control box" points="44,0 88,24 88,76 44,100 0,76 0,24" fill="url(#gSvc3)"/>
</svg>

<!-- reviews -->
<h2 class="display review-title"><span class="navy">Client</span><br><span class="red">Reviews</span></h2>
<div class="circle-btn outline" style="left:67px;top:3927px"><svg width="14" height="14" viewBox="0 0 14 14"><path d="M9 2 L4 7 L9 12" fill="none" stroke="var(--navy)" stroke-width="2.5"/></svg></div>
<div class="circle-btn fill" style="left:135px;top:3927px"><svg width="14" height="14" viewBox="0 0 14 14"><path d="M5 2 L10 7 L5 12" fill="none" stroke="#fff" stroke-width="2.5"/></svg></div>

<div class="abs" style="left:553px;top:3842px;width:222px;height:166px;background:var(--navy);clip-path:polygon(100% 0,100% 100%,0 100%)"></div>
<div class="review-card" style="left:445px">
  <div class="avatar" role="img" aria-label="Customer portrait"><span class="quote-dot">”</span></div>
  <p>Lorem ipsum dolor sit amet, consecte tur adipiscing elit. Pellentesque ali quet eros vitae placerat hendrerit.</p>
  <h4>DORIAN VALE</h4>
  <div class="stars">★★★★★</div>
</div>
<div class="abs" style="left:908px;top:3842px;width:222px;height:166px;background:var(--red);clip-path:polygon(100% 0,100% 100%,0 100%)"></div>
<div class="review-card" style="left:800px">
  <div class="avatar" role="img" aria-label="Customer portrait"><span class="quote-dot" style="background:var(--red)">”</span></div>
  <p>Lorem ipsum dolor sit amet, consecte tur adipiscing elit. Pellentesque ali quet eros vitae placerat hendrerit.</p>
  <h4>DORIAN VALE</h4>
  <div class="stars">★★★★★</div>
</div>

<!-- projects -->
<h2 class="display proj-title"><span class="navy">Our</span> <span class="red">Projects</span></h2>
<div class="proj-img" role="img" aria-label="Gloved hand fitting a steel fence rail" style="left:68px;background:linear-gradient(120deg,#c7c2b8,#8d8a84 60%,#2f3550)"></div>
<div class="proj-img" role="img" aria-label="Welder fabricating a steel gate" style="left:430px;background:linear-gradient(135deg,#1f2b3b,#53606f 55%,#2c241c)"></div>
<div class="proj-img" role="img" aria-label="Tall black metal fence beside a lawn" style="left:790px;background:linear-gradient(90deg,#d2d1cb,#4a4b45 50%,#7f8a55)"></div>
<div class="circle-btn outline" style="left:537px;top:4679px"><svg width="14" height="14" viewBox="0 0 14 14"><path d="M9 2 L4 7 L9 12" fill="none" stroke="var(--navy)" stroke-width="2.5"/></svg></div>
<div class="circle-btn fill" style="left:607px;top:4679px"><svg width="14" height="14" viewBox="0 0 14 14"><path d="M5 2 L10 7 L5 12" fill="none" stroke="#fff" stroke-width="2.5"/></svg></div>

<!-- footer -->
<footer class="site-footer">
  <div class="footer-brand"><span class="brand-mark" style="width:34px;height:34px"></span>Yardline Works</div>
  <div class="footer-col" style="left:546px">
    <h5><span class="navy">Quick</span> <span class="red">Links</span></h5>
    <ul class="links"><li>About Us</li><li>Services</li><li>Projects</li><li>Reviews</li><li>Contact Us</li></ul>
  </div>
  <div class="footer-col" style="left:788px">
    <h5><span class="navy">Contact</span> <span class="red">Us</span></h5>
    <div class="contact-row"><span class="c-icon"><svg width="14" height="14" viewBox="0 0 14 14"><path d="M3 1 l3 3 -1.5 2 q1.5 3 4 4 l2 -1.5 3 3 -2 2 q-6 0 -10.5 -10.5z" fill="#fff"/></svg></span><span>CALL US<br>5550 184 2273</span></div>
    <div class="contact-row"><span class="c-icon"><svg width="14" height="12" viewBox="0 0 14 12"><rect x="1" y="1" width="12" height="10" fill="none" stroke="#fff" stroke-width="1.6"/><path d="M1 1 L7 6 L13 1" fill="none" stroke="#fff" stroke-width="1.6"/></svg></span><span>EMAIL US<br>hello@yardlineworks.example</span></div>
    <div class="contact-row"><span class="c-icon"><svg width="12" height="14" viewBox="0 0 12 14"><path d="M6 14 C1 8 1 6 1 5 a5 5 0 0 1 10 0 c0 1 0 3 -5 9z" fill="#fff"/><circle cx="6" cy="5" r="2" fill="var(--red)"/></svg></span><span>Address line dummy here<br>Addres line dummy here</span></div>
  </div>
</footer>
<div class="bottom-bar">
  <span class="abs" style="left:65px;top:31px">Copyright © 2025 All Rights Reserved By Company name</span>
  <div class="socials"><span></span><span></span><span></span><span></span></div>
</div>

</body>
</html>
```